Business Card- Can you make it cool vs boring!

Need a refresh on my business card! Want it to be modern but simple, classic and a pop of coolness! we do senior living and it is boring. but that doesn't mean our business card have to look boring! Open to two sided cards. our website is www.Bruvel-HQ.com

Target Market(s)

capital market

Industry/Entity Type

senior housing/ real estate

Contact Information for Business Card

logo/ name/ cell/ address/ www.bruvel-hq.com/ space for a QR code

Requirements
Must have
• maybe a QR code (do not make prominent I may not use the QR so design where it can be taken out) that link to more about us/ landing page. needs to be modern but clean
Should not have
• clip art or script

```html
<!DOCTYPE html>
<html lang="en">
<head>
<meta charset="utf-8">
<title>Bruvel Living – Business Card</title>
<link rel="stylesheet" href="https://fonts.googleapis.com/css2?family=PT+Sans:wght@400;700&display=swap">
<style>
  :root {
    --rust: #b04b26;
    --stone: #8d8589;
    --ink: #1c1c1c;
    --paper: #ffffff;
    --backdrop: #b1b0ae;
  }
  * { box-sizing: border-box; margin: 0; padding: 0; }
  html, body { width: 900px; height: 1200px; overflow: hidden; }
  body {
    background: var(--backdrop);
    font-family: "PT Sans", sans-serif;
    color: var(--ink);
    position: relative;
  }
  .card {
    position: absolute;
    left: 88px;
    width: 724px;
    height: 415px;
    border-radius: 33px;
    overflow: hidden;
  }
  .card--front { top: 125px; background: var(--rust); }
  .card--back { top: 575px; background: var(--paper); }

  .front-band {
    position: absolute; left: 0; right: 0; bottom: 0; height: 27px;
    background: var(--stone);
  }
  .front-brand {
    position: absolute; left: 0; right: 0; top: 160px;
    text-align: center;
    font-size: 82px; font-weight: 400; line-height: 1;
    color: var(--paper);
    letter-spacing: 1px;
  }

  .back-brand {
    position: absolute; left: 24px; top: 48px;
    font-size: 40px; font-weight: 400; line-height: 1;
    color: var(--rust);
  }
  .person {
    position: absolute; right: 25px; top: 203px; text-align: right;
  }
  .person__name {
    font-size: 28px; font-weight: 700; color: var(--rust); line-height: 1;
    letter-spacing: 0.3px;
  }
  .person__role { font-size: 18px; margin-top: 8px; line-height: 1; }
  .accent-bar {
    position: absolute; right: 0; top: 208px; width: 17px; height: 47px;
    background: var(--rust);
  }
  .rule {
    position: absolute; left: 24px; top: 242px; width: 597px; height: 2px;
    background: var(--rust);
  }
  .contacts {
    position: absolute; left: 24px; top: 307px; list-style: none;
    font-size: 19px; line-height: 26px;
  }
  .contacts li { display: flex; align-items: center; gap: 9px; }
  .contacts svg { width: 16px; height: 16px; fill: var(--rust); flex: none; }
  .address {
    position: absolute; right: 25px; top: 333px; text-align: right;
    font-size: 19px; line-height: 26px; font-style: normal;
  }
  .back-band {
    position: absolute; left: 0; right: 0; bottom: 0; height: 26px;
    background: var(--rust);
  }
</style>
</head>
<body>
  <section class="card card--front">
    <div class="front-brand">Bruvel Living</div>
    <div class="front-band"></div>
  </section>

  <section class="card card--back">
    <div class="back-brand">Bruvel Living</div>

    <div class="person">
      <div class="person__name">DANIEL MARSH</div>
      <div class="person__role">Owner</div>
    </div>
    <div class="accent-bar"></div>
    <div class="rule"></div>

    <ul class="contacts">
      <li>
        <svg viewBox="0 0 16 16" aria-hidden="true"><path d="M2 5c0-2 3-3 6-3s6 1 6 3v1h-3V5H5v1H2z"/><rect x="3" y="7" width="10" height="7" rx="1"/></svg>
        (555) 014-2270
      </li>
      <li>
        <svg viewBox="0 0 16 16" aria-hidden="true"><path d="M1 3h14v10H1z M2 4l6 5 6-5" fill="none" stroke="currentColor"/><path d="M1 3h14v1.5L8 10 1 4.5z M1 5.5l5 4-5 3.5z M15 5.5l-5 4 5 3.5z M6.8 10.3 8 11.3l1.2-1L14.5 13h-13z"/></svg>
        info@bruvel-hq.com
      </li>
      <li>
        <svg viewBox="0 0 16 16" aria-hidden="true"><circle cx="8" cy="8" r="7"/><path d="M4 5c1 0 2 1 2 2s-1 1-1 2 1 2 0 3M10 3c-1 1 0 2 1 2s2 1 1 3" stroke="#fff" stroke-width="1.2" fill="none"/></svg>
        www.bruvel-hq.com/
      </li>
    </ul>

    <address class="address">
      4870 Larkmoor Lane, Suite #310<br>
      Cedar Hollow, TX 77500
    </address>

    <div class="back-band"></div>
  </section>
</body>
</html>
```